OLU58 biz card & Stationery

LU58 is a personalized shopping experience brought to you, that lets you find and discover fashion goods through a collection of boutiques curated by taste-makers - celebrities, stylists, designers, and fashion bloggers. Boutiques uses visual technology to help fashionistas discover and shop their look and creates the opportunity for designers to showcase their collections and latest inspirations online.

OLU58 is built on technology developed by our team of fashion experts who work with engineers to “teach” our computer systems to understand various patterns, pairings, and genre definitions. When signed into your account, OLU58 learns about your style and preferences and in turn, provides you better results and recommendations over time. Ultimately, OLU58 will provide shoppers with a much richer and interactive shopping experience and help drive traffic to retailers' websites.

We need a definitely cool business card. The card must be black! And must use our official logo which can be download from OLU58.com

The address for Letter head and evenlop, please use 4872 Crestwick Parkway, Sutie 510 Los Angeles CA90412, email will be anyone@OLU58.com, website is www.OLU58.com

thanks

We received some of the design, thanks. But most of the design are not what we want. We need a very clean version with black ground, you may also use some dark gray to add the element. please take a look at http://morvalstudio.no/work/#pelter__ostrama/, we do like this kind of design very much. hope it help.

```html
<!DOCTYPE html>
<html lang="en">
<head>
<meta charset="utf-8">
<title>OLU58 Letterhead</title>
<link rel="stylesheet" href="https://fonts.googleapis.com/css2?family=Belleza&family=Roboto+Condensed:wght@300;400&display=swap">
<style>
  :root {
    --backdrop: #ffffff;
    --paper: #ffffff;
    --ink-black: #000000;
    --tab-gray: #58585a;
    --text-gray: #6d6e70;
    --text-white: #ffffff;
  }
  * { margin: 0; padding: 0; box-sizing: border-box; }
  html, body {
    width: 1200px;
    height: 900px;
    overflow: hidden;
    background: var(--backdrop);
  }
  .canvas {
    position: relative;
    width: 1200px;
    height: 900px;
  }
  .letterhead {
    position: absolute;
    left: 293px;
    top: 28px;
    width: 598px;
    height: 847px;
    background: var(--paper);
    box-shadow: 2px 3px 4px rgba(0, 0, 0, 0.45);
    overflow: hidden;
  }
  .header-band {
    position: absolute;
    left: 0;
    top: 0;
    width: 100%;
    height: 133px;
    background: var(--ink-black);
  }
  .wordmark {
    position: absolute;
    left: -2px;
    top: 52px;
    font-family: "Belleza", sans-serif;
    font-size: 57px;
    line-height: 1;
    letter-spacing: 1px;
    color: var(--text-white);
  }
  .tagline-tab {
    position: absolute;
    left: 538px;
    top: 0;
    width: 23px;
    height: 160px;
    background: var(--tab-gray);
  }
  .tagline {
    position: absolute;
    left: 50%;
    top: 50%;
    transform: translate(-50%, -50%) rotate(-90deg);
    white-space: nowrap;
    font-family: "Belleza", sans-serif;
    font-size: 10.5px;
    letter-spacing: 0.6px;
    color: var(--text-white);
  }
  .footer-contact {
    position: absolute;
    right: 34px;
    bottom: 20px;
    display: flex;
    align-items: baseline;
    gap: 7px;
    white-space: nowrap;
  }
  .contact-detail {
    font-family: "Roboto Condensed", sans-serif;
    font-weight: 300;
    font-size: 10px;
    color: var(--text-gray);
  }
  .contact-divider {
    font-family: "Roboto Condensed", sans-serif;
    font-weight: 300;
    font-size: 12px;
    color: var(--text-gray);
  }
  .contact-web {
    font-family: "Belleza", sans-serif;
    font-size: 20px;
    letter-spacing: 0.5px;
    color: var(--text-gray);
  }
</style>
</head>
<body>
<div class="canvas">
  <section class="letterhead">
    <header class="header-band">
      <div class="wordmark">OLU58</div>
    </header>
    <div class="tagline-tab">
      <span class="tagline">SOCIAL FASHION ONLINE</span>
    </div>
    <footer class="footer-contact">
      <span class="contact-detail">4872 Crestwick Parkway, Sutie 510, Los Angeles CA90412</span>
      <span class="contact-divider">|</span>
      <span class="contact-detail">anyone@OLU58.com</span>
      <span class="contact-divider">|</span>
      <span class="contact-web">www.OLU58.com</span>
    </footer>
  </section>
</div>
</body>
</html>
```